One page responsive Wordpress Website

I am looking to design and code for 1-page Wordpress responsive website (desktop/mobile/tablet). Pls see attached file. Job scope includes Wordpress design and coding of the actual Live website
Target Market(s)
Small medium business
Industry/Entity Type
Telecommunications
Font styles to use
Sans Serif
Colors
ffffff
85cae6
63bae0
33a6d7
cedeed
3277b5
Requirements
Must have
- One page only, Wordpress, Responsive layout in desktop, mobile, tablet

```html
<!DOCTYPE html>
<html lang="en">
<head>
<meta charset="utf-8">
<title>Voxlane IP Phone</title>
<link href="https://fonts.googleapis.com/css2?family=Montserrat:wght@300;400;500;600;800;900&display=swap" rel="stylesheet">
<style>
  :root{
    --white:#ffffff;
    --sky:#85cae6;
    --aqua:#63bae0;
    --cyan:#33a6d7;
    --mist:#cedeed;
    --brand:#3277b5;
    --deep:#1f68ae;
    --ink:#2b2b35;
    --logo:#1ea6e6;
  }
  *{margin:0;padding:0;box-sizing:border-box}
  html,body{width:760px;height:1200px;overflow:hidden;background:var(--white)}
  body{font-family:'Montserrat',sans-serif;color:var(--ink);position:relative}
  .page{position:relative;width:760px;height:1200px;overflow:hidden}
  .abs{position:absolute}
  .hero-bg{left:0;top:0;width:760px;height:380px}
  .map{left:48px;top:70px;width:610px;height:160px;border-radius:80px;
    background:radial-gradient(ellipse at 50% 60%,rgba(99,186,224,.55),rgba(51,166,215,0) 70%)}
  .logo{left:102px;top:12px;font-weight:800;font-size:31px;color:var(--logo);letter-spacing:-.5px}
  .nav{right:102px;top:24px;display:flex;gap:28px;font-size:9px;font-weight:500;color:var(--white)}
  .hero-text{left:0;width:760px;text-align:center;color:var(--white)}
  .eyebrow{top:89px;font-size:15px;font-weight:300}
  .title{top:113px;font-size:30px;font-weight:900}
  .lead{top:159px;font-size:9px;line-height:12px;font-weight:400}
  .card{top:231px;width:176px;height:197px;background:var(--white);border-radius:4px;overflow:hidden;
    box-shadow:0 6px 18px rgba(31,104,174,.18)}
  .card h3{position:absolute;top:15px;width:100%;text-align:center;font-weight:500;font-size:14px;color:var(--brand)}
  .product{position:absolute;top:49px;left:50%;transform:translateX(-50%);width:70px;height:80px;border-radius:4px;
    background:linear-gradient(160deg,#5a6470,#2c333c)}
  .features{position:absolute;top:139px;width:100%;display:flex;justify-content:center;gap:4px}
  .features span{width:19px;height:19px;border-radius:50%;background:var(--mist);border:1px solid #b9cde3}
  .download{position:absolute;bottom:0;left:0;width:100%;height:28px;background:var(--brand);color:var(--white);
    font-size:9px;font-weight:600;display:flex;align-items:center;justify-content:center;gap:7px}
  .section-h{font-weight:900;font-size:22px;color:var(--brand)}
  .about-h{left:102px;top:485px}
  .about-p{left:102px;top:527px;width:300px;font-size:9.5px;line-height:17.2px}
  .about-img{left:460px;top:494px;width:180px;height:180px;border-radius:6px;
    background:linear-gradient(150deg,#4b5563,#2a3140 60%,#1f2836)}
  .contact-band{left:0;top:720px;width:760px;height:310px}
  .contact-h{left:102px;top:843px}
  .contact-p{left:102px;top:880px;width:255px;font-size:9.5px;line-height:17.2px}
  .contact-p p+p{margin-top:6px}
  .people{left:403px;top:848px;width:257px;height:130px;border-radius:10px 10px 0 0;
    background:linear-gradient(135deg,#6f9be8,#2d4fc9 55%,#8bb4f0)}
  .footer{left:0;top:1030px;width:760px;height:170px;background:var(--brand);color:var(--white)}
  .f-logo{position:absolute;left:102px;top:24px;font-weight:800;font-size:28px}
  .f-links{position:absolute;left:102px;top:73px;font-size:9px;line-height:14.5px;list-style:none}
  .f-links li{display:flex;align-items:center;gap:6px}
  .f-links li::before{content:"";width:6px;height:6px;border:1.5px solid var(--white);border-radius:50%}
  .f-h{position:absolute;left:315px;top:36px;font-size:11px;font-weight:600}
  .f-item{position:absolute;display:flex;align-items:center;gap:8px;font-size:8px;line-height:12.5px}
  .f-icon{width:19px;height:19px;background:var(--white);border-radius:2px;display:flex;align-items:center;justify-content:center;flex:none}
  .f-rule{position:absolute;left:102px;right:102px;top:1144px;border-top:1px solid rgba(255,255,255,.35)}
  .copy{position:absolute;left:0;width:760px;top:1153px;text-align:center;font-size:7px}
</style>
</head>
<body>
<div class="page">
  <svg class="abs hero-bg" viewBox="0 0 760 380" aria-hidden="true">
    <defs>
      <linearGradient id="heroGrad" x1="0" y1="0" x2="0" y2="1">
        <stop offset="0" stop-color="#2f72b8"/>
        <stop offset=".6" stop-color="#2a8cc5"/>
        <stop offset="1" stop-color="#1a80bf"/>
      </linearGradient>
    </defs>
    <path d="M0 0H760V325C640 290 520 300 420 330C330 355 250 365 150 340C90 325 40 310 0 300Z" fill="url(#heroGrad)"/>
  </svg>
  <div class="abs map" role="img" aria-label="Faint world map backdrop"></div>

  <div class="abs logo">Voxlane</div>
  <nav class="abs nav"><span>About Us</span><span>Contact Us</span></nav>

  <div class="abs hero-text eyebrow">Enterprise HD IP Phone</div>
  <h1 class="abs hero-text title">Voxlane IP Phone</h1>
  <p class="abs hero-text lead">The most affordable IP Phone, with highest compatibility to<br>every IP-PBX system. Sleek designed and user-friendly proven.</p>

  <div class="abs card" style="left:102px">
    <h3>Voxlane VL310G</h3>
    <div class="product" role="img" aria-label="Desk IP phone with handset and colour screen"></div>
    <div class="features"><span></span><span></span><span></span><span></span></div>
    <div class="download">Download Datasheet (En)
      <svg width="13" height="14" viewBox="0 0 13 14" fill="none" stroke="#fff" stroke-width="1"><path d="M2 1h6l3 3v5M2 1v12h5"/><circle cx="9" cy="11" r="3"/><path d="M9 9.5v3M7.8 11.4 9 12.5l1.2-1.1"/></svg>
    </div>
  </div>
  <div class="abs card" style="left:293px">
    <h3>Voxlane VL350G</h3>
    <div class="product" role="img" aria-label="Desk IP phone with side keys and colour screen"></div>
    <div class="features"><span></span><span></span><span></span><span></span><span></span><span></span></div>
    <div class="download">Download Datasheet (En)
      <svg width="13" height="14" viewBox="0 0 13 14" fill="none" stroke="#fff" stroke-width="1"><path d="M2 1h6l3 3v5M2 1v12h5"/><circle cx="9" cy="11" r="3"/><path d="M9 9.5v3M7.8 11.4 9 12.5l1.2-1.1"/></svg>
    </div>
  </div>
  <div class="abs card" style="left:483px">
    <h3>Voxlane VL40</h3>
    <div class="product" style="width:50px" role="img" aria-label="Expansion module with key list screen"></div>
    <div class="download">Download Datasheet (En)
      <svg width="13" height="14" viewBox="0 0 13 14" fill="none" stroke="#fff" stroke-width="1"><path d="M2 1h6l3 3v5M2 1v12h5"/><circle cx="9" cy="11" r="3"/><path d="M9 9.5v3M7.8 11.4 9 12.5l1.2-1.1"/></svg>
    </div>
  </div>

  <h2 class="abs section-h about-h">About us</h2>
  <p class="abs about-p">Voxlane IP Phones is designed with pixel colour LCD with backlight LED, built-in Gigabit Ethernet with up to 28 various features. Equipped with Power over Ethernet (PoE) support, and high definition (HD) sound quality with a rich visual experience. Designed with a fresh appearance, it supports flexible and secured provisioning, deliver modern elegant appearance, superb sound quality and a rich set of IP/SIP telephony features.</p>
  <div class="abs about-img" role="img" aria-label="IP desk phone in front of an expansion module"></div>

  <svg class="abs contact-band" viewBox="0 0 760 310" aria-hidden="true">
    <path d="M0 20C90 55 170 75 270 75C400 75 520 25 640 25C700 25 740 32 760 38V310H0Z" fill="var(--mist)"/>
  </svg>
  <h2 class="abs section-h contact-h">Contact Us Now</h2>
  <div class="abs contact-p">
    <p>Speak to us or send us an enquiry for free consultation.</p>
    <p>Our team would love to share more about Voxlane IP Phones. We are expecting your calls and emails. Drop us an enquiry form at your fingertips!</p>
  </div>
  <div class="abs people" role="img" aria-label="Illustration of a team gathered around a laptop"></div>

  <footer class="abs footer">
    <div class="f-logo">Voxlane</div>
    <ul class="f-links"><li>About Us</li><li>Contact Us</li></ul>
    <div class="f-h">Contact Us</div>
    <div class="f-item" style="left:316px;top:63px">
      <span class="f-icon"><svg width="11" height="11" viewBox="0 0 11 11" fill="none" stroke="#3277b5"><path d="M5.5 1a2.5 2.5 0 0 1 2.5 2.5C8 5.5 5.5 8 5.5 8S3 5.5 3 3.5A2.5 2.5 0 0 1 5.5 1Z"/><path d="M1 10h9"/></svg></span>
      <span>48 Harbour Lane, #05-12,<br>Singapore 100482</span>
    </div>
    <div class="f-item" style="left:316px;top:98px">
      <span class="f-icon"><svg width="11" height="9" viewBox="0 0 11 9" fill="none" stroke="#3277b5"><rect x=".5" y=".5" width="10" height="8"/><path d="M.5.5 5.5 5l5-4.5"/></svg></span>
      <span>enquiry@voxlanetel.com</span>
    </div>
    <div class="f-item" style="left:500px;top:64px">
      <span class="f-icon"><svg width="11" height="11" viewBox="0 0 11 11" fill="none" stroke="#3277b5"><path d="M2 1h2l1 2.5-1.3 1a6 6 0 0 0 2.8 2.8l1-1.3L10 7v2a1 1 0 0 1-1 1A8 8 0 0 1 1 2a1 1 0 0 1 1-1Z"/></svg></span>
      <span>6100-2300</span>
    </div>
    <div class="f-item" style="left:500px;top:93px">
      <span class="f-icon"></span>
      <span>6100-2300</span>
    </div>
    <div class="f-rule" style="top:114px"></div>
    <div class="copy" style="top:123px">© Voxlane 2021</div>
  </footer>
</div>
</body>
</html>
```